Mental Health

KVR HAVEN
Behavioral Health
4172 E. Dorrel St. Mesa, AZ 85217
Marguerite (480)555-0142 / Ivan 480-555-0187

Email: KVRHaven@Qortamail.com
Newly Remodeled & Spacious
g Staff
Registered Nurses
Licensed Independent &
Professional Substance &
Abuse Counselors
Behavioral Health Techs
Certified Caregivers
Behavioral Health &
Substance Abuse Professionals

To Refer a Patient
About Us
KVR Haven is a Fully Staffed Behavioral
Health Residential Facility, providing
treatment plans for adults suffering
with various Behavioral Health and
Substance Abuse disorders, while living
in a nice safe, clean and supportive
environment. Our home offers clients the
ability to learn the necessary skills to
help clients adapt, build self confidence
as well as independence, with the goal
of reducing the probability of a future
crisis or possible relapse. We offer
counseling programs, consisting of a
variety of addiction and recovery support
groups, independent living, coping and
social skills groups, as well as assisting
clients with using tools to create a resume
to help obtain employment and so much
more. We are committed to teaching
self management care and allowing
clients to understand how to utilize the
resources, skills and tools available for
long term success by providing superior
quality, all-inclusive living arrangements
and treatment options.

Thank you for your patience while I update the final content needed for us to make the final decision this week.

```html
<!DOCTYPE html>
<html lang="en">
<head>
<meta charset="utf-8">
<title>KVR Haven Behavioral Health – Business Cards</title>
<link rel="stylesheet" href="https://fonts.googleapis.com/css2?family=Montserrat:wght@400;500&family=Courgette&display=swap">
<style>
  :root {
    --bg: #d3d5d7;
    --card: #ffffff;
    --ink: #555759;
    --brand-blue: #1b73bd;
    --brand-green: #7ab648;
    --dot-blue: #3b7fd0;
    --dot-purple: #6a3a9c;
    --dot-red: #d8262c;
    --dot-yellow: #f2b51c;
    --dot-green: #6cb33f;
    --phone-red: #d8262c;
    --phone-purple: #6a3a9c;
    --pin-orange: #ef7d23;
    --mail-pink: #e0338a;
  }
  * { margin: 0; padding: 0; box-sizing: border-box; }
  html, body { width: 1200px; height: 928px; overflow: hidden; }
  body {
    background: var(--bg);
    font-family: "Montserrat", sans-serif;
    color: var(--ink);
    position: relative;
  }
  .card {
    position: absolute;
    left: 260px;
    width: 680px;
    height: 388px;
    background: var(--card);
    border-radius: 30px;
    box-shadow: 0 6px 18px rgba(0,0,0,0.18);
  }
  .card--front { top: 48px; }
  .card--back { top: 492px; }

  .brand {
    position: absolute;
    left: 0; right: 0;
    display: flex;
    flex-direction: column;
    align-items: center;
  }
  .brand__row { display: flex; align-items: center; gap: 16px; }
  .brand__mark {
    width: 62px; height: 62px; border-radius: 50%;
    background: var(--brand-green);
  }
  .brand__name {
    font-size: 46px;
    font-weight: 400;
    letter-spacing: 2px;
    color: var(--brand-blue);
    line-height: 1;
  }
  .brand__tagline {
    margin-top: 10px;
    font-size: 21px;
    letter-spacing: 3px;
    color: var(--ink);
  }
  .card--front .brand { top: 70px; }
  .card--back .brand { top: 140px; }

  .services {
    position: absolute;
    top: 216px; left: 0; right: 0;
    display: grid;
    grid-template-columns: 1fr 22px 1fr;
    row-gap: 6px;
    font-size: 15px;
    line-height: 20px;
  }
  .services__left { text-align: right; }
  .services__dot {
    width: 9px; height: 9px; border-radius: 50%;
    align-self: center; justify-self: center;
  }
  .dot--blue { background: var(--dot-blue); }
  .dot--purple { background: var(--dot-purple); }
  .dot--red { background: var(--dot-red); }
  .dot--yellow { background: var(--dot-yellow); }
  .dot--green { background: var(--dot-green); }

  .contact { position: absolute; }
  .contact__name {
    font-family: "Courgette", cursive;
    font-size: 26px;
    line-height: 1.1;
  }
  .contact__line {
    display: flex; align-items: center; gap: 6px;
    font-size: 15px;
  }
  .contact--primary { top: 40px; left: 48px; }
  .contact--primary .contact__name { color: var(--brand-blue); }
  .contact--secondary { top: 40px; right: 48px; text-align: right; }
  .contact--secondary .contact__name { color: var(--brand-green); }
  .contact--email { top: 250px; right: 48px; }
  .contact--address { bottom: 40px; left: 48px; }
  .icon { width: 15px; height: 15px; flex: none; }
</style>
</head>
<body>

<section class="card card--front" aria-label="Card front">
  <div class="brand">
    <div class="brand__row">
      <span class="brand__mark"></span>
      <span class="brand__name">KVR HAVEN</span>
    </div>
    <div class="brand__tagline">BEHAVIORAL HEALTH</div>
  </div>
  <div class="services">
    <span class="services__left">Newly Remodeled</span><span class="services__dot dot--blue"></span><span>Abuse Counselors</span>
    <span class="services__left">Spaciousg Staff</span><span class="services__dot dot--purple"></span><span>Behavioral Health Techs</span>
    <span class="services__left">Registered Nurses</span><span class="services__dot dot--red"></span><span>Certified Caregivers</span>
    <span class="services__left">Licensed Independent</span><span class="services__dot dot--yellow"></span><span>Behavioral Health</span>
    <span class="services__left">Professional Substance</span><span class="services__dot dot--green"></span><span>Substance Abuse Professionals</span>
  </div>
</section>

<section class="card card--back" aria-label="Card back">
  <div class="contact contact--primary">
    <div class="contact__name">Marguerite</div>
    <div class="contact__line">
      <svg class="icon" viewBox="0 0 16 16"><path d="M3 1.5l3 3-1.6 1.8a9 9 0 0 0 5.3 5.3L11.5 10l3 3-1.8 2C6.5 15 1 9.5 1 3.3z" fill="var(--phone-red)"/></svg>
      (480)555-0142
    </div>
  </div>
  <div class="contact contact--secondary">
    <div class="contact__name">Ivan</div>
    <div class="contact__line">
      <svg class="icon" viewBox="0 0 16 16"><path d="M3 1.5l3 3-1.6 1.8a9 9 0 0 0 5.3 5.3L11.5 10l3 3-1.8 2C6.5 15 1 9.5 1 3.3z" fill="var(--phone-purple)"/></svg>
      480-555-0187
    </div>
  </div>

  <div class="brand">
    <div class="brand__row">
      <span class="brand__mark"></span>
      <span class="brand__name">KVR HAVEN</span>
    </div>
    <div class="brand__tagline">BEHAVIORAL HEALTH</div>
  </div>

  <div class="contact contact--email">
    <div class="contact__line">
      <svg class="icon" viewBox="0 0 16 16"><rect x="1" y="3" width="14" height="10" fill="var(--mail-pink)"/><path d="M1 3l7 6 7-6" fill="none" stroke="#fff" stroke-width="1.4"/></svg>
      KVRHaven@Qortamail.com
    </div>
  </div>
  <div class="contact contact--address">
    <div class="contact__line">
      <svg class="icon" viewBox="0 0 16 16"><path d="M8 1a5 5 0 0 0-5 5c0 4 5 9 5 9s5-5 5-9a5 5 0 0 0-5-5z" fill="var(--pin-orange)"/><circle cx="8" cy="6" r="2" fill="#fff"/></svg>
      4172 E. Dorrel St. Mesa, AZ 85217
    </div>
  </div>
</section>

</body>
</html>
```